The Brightwell Clinic :

At The Brightwell Clinic our goal is to provide the most skilled and advanced examination and treatment of the upper neck for superior long-term outcomes for those experiencing headache or migraine.

If a spinal disorder is responsible for the headache and migraine condition the disorder will involve one or more of the top three spinal segments. The fundamental and most powerful feature of The Brightwell Clinic is our method of examining the movements of the top three spinal segments.

We would like the design should communicate professionalism and specialisation.
Updates

Don't necessarily have to have the photos provided.Photo was used for promotional material. I dont have a logo as yet what I  would also like designed.

Project Deadline Extended
Reason: Opening has been delayed due to construction issues of building.

Industry/Entity Type

Clinic

Contact Information for Business Card

The Brightwell Clinic
Suite 3, Oakvale Heath Centre
87 Ferncliff Drive, Coralbrook NSW 2471
Tel : 63 71 2946 www.thebrightwellclinic.com.au

Requirements
Must have
• Mr Carl Pettigrew
Senior Physiotherapist / Senior Accredited Exercise Physiologist
B. Hlth. Sc. (Physiotherapy), B. Mov. Sc. (Exercise Science), Dip. M.T., Member, Coastal Allied Health Guild.

Appointment area on back of card

```html
<!DOCTYPE html>
<html lang="en">
<head>
<meta charset="utf-8">
<title>The Brightwell Clinic – Business Card</title>
<link rel="stylesheet" href="https://fonts.googleapis.com/css2?family=Alegreya+Sans+SC:wght@700&family=Cinzel:wght@600&family=PT+Sans:ital,wght@0,400;0,700;1,400&display=swap">
<style>
  :root {
    --backdrop: #b9542a;
    --card: #ffffff;
    --brand-green: #8dbb3c;
    --name-purple: #6b2d7c;
    --heading-green: #1f4f2c;
    --text-grey: #555555;
    --text-dark: #3d3d3d;
    --rule-grey: #8a8a8a;
  }
  * { box-sizing: border-box; margin: 0; padding: 0; }
  html, body { width: 1200px; height: 405px; overflow: hidden; }
  body { background: var(--backdrop); position: relative; font-family: "PT Sans", sans-serif; }

  .card {
    position: absolute; top: 47px; width: 535px; height: 306px;
    background: var(--card); border-radius: 28px;
  }
  .card--front { left: 57px; }
  .card--back { left: 619px; }

  .line { position: absolute; left: 0; right: 0; text-align: center; line-height: 1; white-space: nowrap; }
  .brand { font-family: "Alegreya Sans SC", sans-serif; font-weight: 700; color: var(--brand-green); font-size: 30px; letter-spacing: 3.4px; }

  .side-tab { position: absolute; top: 93px; width: 8px; height: 121px; background: var(--brand-green); }
  .side-tab--left { left: -2px; border-radius: 0 4px 4px 0; }
  .side-tab--right { right: -2px; border-radius: 4px 0 0 4px; }

  .practitioner { font-family: "Alegreya Sans SC", sans-serif; font-weight: 700; color: var(--name-purple); font-size: 17px; letter-spacing: 2px; }
  .credentials { color: var(--text-grey); font-size: 11.5px; }
  .phone { font-family: "Alegreya Sans SC", sans-serif; font-weight: 700; color: var(--brand-green); font-size: 27px; letter-spacing: 3.5px; }
  .address { color: var(--text-grey); font-size: 14.5px; }
  .website { color: var(--text-grey); font-size: 12.5px; letter-spacing: 2.4px; }

  .appointment-title { font-family: "Cinzel", serif; font-weight: 600; color: var(--heading-green); font-size: 18.5px; }
  .field-label { position: absolute; color: var(--text-dark); font-size: 15.5px; line-height: 1; white-space: nowrap; }
  .rule { position: absolute; height: 0; border-bottom: 1px solid var(--rule-grey); }
  .rule--dotted { border-bottom-style: dotted; }
  .box { position: absolute; border: 1px solid var(--text-grey); border-radius: 2px; }
  .day { position: absolute; font-weight: 700; color: var(--text-grey); font-size: 15px; line-height: 1; }
  .notice { color: var(--text-grey); font-size: 15.5px; font-style: italic; }
</style>
</head>
<body>
  <section class="card card--front">
    <span class="side-tab side-tab--left"></span>
    <span class="side-tab side-tab--right"></span>
    <p class="line brand" style="top:24px">The Brightwell Clinic</p>
    <p class="line practitioner" style="top:89px">Mr Carl Pettigrew</p>
    <p class="line credentials" style="top:110px">Senior Physiotherapist / Senior Accredited Exercise Physiologist</p>
    <p class="line credentials" style="top:124px">B. Hlth. Sc. (Physiotherapy), B. Mov. Sc. (Exercise Science), Dip. M.T.</p>
    <p class="line credentials" style="top:138px">Member, Coastal Allied Health Guild.</p>
    <p class="line phone" style="top:168px">Tel : 63 71 2946</p>
    <p class="line address" style="top:216px">Suite 3, Oakvale Heath Centre 87</p>
    <p class="line address" style="top:234px">Ferncliff Drive, Coralbrook NSW 2471</p>
    <p class="line website" style="top:271px">www.thebrightwellclinic.com.au</p>
  </section>

  <section class="card card--back">
    <p class="line brand" style="top:26px">The Brightwell Clinic</p>
    <p class="line appointment-title" style="top:76px">YOUR APPOINTMENT</p>

    <span class="field-label" style="left:90px;top:114px">Name :</span>
    <span class="rule rule--dotted" style="left:149px;width:297px;top:128px"></span>

    <span class="field-label" style="left:87px;top:151px">Date :</span>
    <span class="rule" style="left:147px;width:96px;top:165px"></span>
    <span class="field-label" style="left:249px;top:151px">Time :</span>
    <span class="rule" style="left:296px;width:92px;top:165px"></span>
    <span class="field-label" style="left:390px;top:151px">am / pm</span>

    <span class="field-label" style="left:94px;top:190px">Next Appointment</span>
    <span class="box" style="left:238px;top:187px;width:96px;height:21px"></span>
    <span class="box" style="left:345px;top:187px;width:96px;height:21px"></span>

    <span class="day" style="left:33px;top:230px">MON</span>
    <span class="box" style="left:80px;top:227px;width:34px;height:20px"></span>
    <span class="day" style="left:120px;top:230px">TUE</span>
    <span class="box" style="left:157px;top:227px;width:34px;height:20px"></span>
    <span class="day" style="left:198px;top:230px">WED</span>
    <span class="box" style="left:241px;top:227px;width:34px;height:20px"></span>
    <span class="day" style="left:281px;top:230px">THU</span>
    <span class="box" style="left:321px;top:227px;width:34px;height:20px"></span>
    <span class="day" style="left:362px;top:230px">FRI</span>
    <span class="box" style="left:392px;top:227px;width:34px;height:20px"></span>
    <span class="day" style="left:432px;top:230px">SAT</span>
    <span class="box" style="left:467px;top:227px;width:34px;height:20px"></span>

    <p class="line notice" style="top:268px">We appreciate a 24 hr. notice for cancellations</p>
  </section>
</body>
</html>
```